Antibacterial Hand Wash Squeeze Tube Label

We're looking for a contemporary label design for a new Antibacterial Hand Wash for an 8oz squeeze tube. The new consumer brand will be sold to consumers in major US retail stores & online. The moisturizing hand wash contains Aloe Vera, vitamin E, and other natural ingredients so the design should include the color green. Real photos are very effective on packaging, so a picture of Aloe Vera or possibly two hands washing would help draw consumers' attention to the tube on the retail shelf. The front label may wrap around the sides. Rear must be left mostly blank
US Consumers - retail stores & online
Consumer

```html
<!DOCTYPE html>
<html lang="en">
<head>
<meta charset="utf-8">
<title>Antibacterial Hand Wash – Tube Label Layout</title>
<link rel="stylesheet" href="https://fonts.googleapis.com/css2?family=Arimo:wght@400;700&display=swap">
<style>
  :root {
    --page: #ffffff;
    --ink: #000000;
    --label-light: #a6d84a;
    --label-mid: #5fb53a;
    --label-deep: #2f8a36;
    --band-dark: rgba(30, 110, 40, 0.35);
    --rule-lime: #d7f04a;
    --rule-green: #3f9a2a;
    --white: #ffffff;
    --pill: #3b8f2c;
    --vitamin: #5aa83a;
  }
  html, body {
    margin: 0;
    padding: 0;
    width: 1200px;
    height: 1000px;
    overflow: hidden;
    background: var(--page);
  }
  .label-sheet {
    display: block;
    width: 1200px;
    height: 1000px;
    font-family: "Arimo", Arial, sans-serif;
  }
  .title-main { fill: var(--white); font-size: 46px; }
  .title-sub { fill: var(--white); font-size: 24px; letter-spacing: 0.5px; }
  .icon-caption { fill: var(--white); font-size: 13px; }
  .benefit-item { fill: var(--white); font-size: 13px; }
  .back-title { fill: var(--white); font-size: 26px; }
  .back-sub { fill: var(--white); font-size: 14px; letter-spacing: 0.4px; }
  .volume-text { fill: var(--white); font-weight: 700; }
  .dieline { fill: none; stroke: var(--ink); stroke-width: 2; }
  .fold-line { stroke: var(--ink); stroke-width: 2; stroke-dasharray: 3 4; }
  .dimension-line { stroke: var(--ink); stroke-width: 2; }
  .dimension-text { fill: var(--ink); font-size: 36px; }
  .icon-fill { fill: var(--white); }
  .icon-stroke { fill: none; stroke: var(--white); }
</style>
</head>
<body>
<svg class="label-sheet" viewBox="0 0 1200 1000" xmlns="http://www.w3.org/2000/svg">
  <defs>
    <linearGradient id="label-gradient" x1="0" y1="0" x2="1" y2="1">
      <stop offset="0" stop-color="var(--label-light)"/>
      <stop offset="0.45" stop-color="var(--label-mid)"/>
      <stop offset="0.75" stop-color="var(--label-deep)"/>
      <stop offset="1" stop-color="var(--label-light)"/>
    </linearGradient>
    <linearGradient id="rule-gradient" x1="0" y1="0" x2="1" y2="0">
      <stop offset="0" stop-color="var(--rule-green)"/>
      <stop offset="0.5" stop-color="var(--rule-lime)"/>
      <stop offset="0.8" stop-color="var(--rule-green)"/>
      <stop offset="1" stop-color="var(--rule-lime)"/>
    </linearGradient>
    <marker id="arrow-head" viewBox="0 0 10 10" refX="9" refY="5" markerWidth="9" markerHeight="9" orient="auto-start-reverse">
      <path d="M0,0 L10,5 L0,10 z" fill="var(--ink)"/>
    </marker>

    <symbol id="icon-no-germs" viewBox="-30 -30 60 60">
      <circle class="icon-fill" r="27"/>
      <circle r="22" fill="var(--label-mid)"/>
      <g class="icon-fill">
        <circle r="10"/>
        <circle cx="0" cy="-15" r="3"/><circle cx="0" cy="15" r="3"/>
        <circle cx="-15" cy="0" r="3"/><circle cx="15" cy="0" r="3"/>
        <circle cx="-11" cy="-11" r="3"/><circle cx="11" cy="11" r="3"/>
        <circle cx="11" cy="-11" r="3"/><circle cx="-11" cy="11" r="3"/>
      </g>
      <line x1="-17" y1="-17" x2="17" y2="17" stroke="var(--label-mid)" stroke-width="8"/>
      <line x1="-17" y1="-17" x2="17" y2="17" stroke="var(--white)" stroke-width="4"/>
    </symbol>

    <symbol id="icon-hands-drop" viewBox="-36 -28 72 56">
      <path class="icon-fill" d="M0,-24 C5,-14 10,-8 10,-2 A10,10 0 0 1 -10,-2 C-10,-8 -5,-14 0,-24 z"/>
      <path class="icon-fill" d="M-6,26 L-6,12 C-10,6 -18,4 -20,-6 L-26,-18 C-28,-22 -24,-24 -22,-20 L-18,-10 L-24,-22 C-25,-26 -21,-27 -20,-23 L-14,-10 C-16,-4 -12,4 -6,8 z"/>
      <path class="icon-fill" d="M-8,26 L-14,26 L-16,14 C-24,8 -32,-2 -34,-14 C-34,-18 -30,-18 -30,-14 C-28,-6 -22,2 -14,8 z"/>
      <g transform="scale(-1,1)">
        <path class="icon-fill" d="M-6,26 L-6,12 C-10,6 -18,4 -20,-6 L-26,-18 C-28,-22 -24,-24 -22,-20 L-18,-10 L-24,-22 C-25,-26 -21,-27 -20,-23 L-14,-10 C-16,-4 -12,4 -6,8 z"/>
        <path class="icon-fill" d="M-8,26 L-14,26 L-16,14 C-24,8 -32,-2 -34,-14 C-34,-18 -30,-18 -30,-14 C-28,-6 -22,2 -14,8 z"/>
      </g>
    </symbol>

    <symbol id="icon-aloe" viewBox="-40 -30 80 60">
      <g class="icon-fill">
        <path d="M0,28 C-6,10 -4,-10 0,-28 C4,-10 6,10 0,28 z"/>
        <path d="M-2,28 C-14,14 -20,-4 -18,-22 C-10,-6 -4,10 -2,28 z"/>
        <path d="M2,28 C14,14 20,-4 18,-22 C10,-6 4,10 2,28 z"/>
        <path d="M-4,28 C-20,22 -32,8 -38,-8 C-24,2 -12,14 -4,28 z"/>
        <path d="M4,28 C20,22 32,8 38,-8 C24,2 12,14 4,28 z"/>
      </g>
    </symbol>

    <symbol id="icon-vitamin-drop" viewBox="-22 -30 44 60">
      <path class="icon-fill" d="M0,-28 C8,-14 18,-2 18,10 A18,18 0 0 1 -18,10 C-18,-2 -8,-14 0,-28 z"/>
      <text x="0" y="8" text-anchor="middle" font-size="12" fill="var(--vitamin)" font-family="Arimo, Arial, sans-serif">E</text>
      <text x="0" y="19" text-anchor="middle" font-size="6.5" fill="var(--vitamin)" font-family="Arimo, Arial, sans-serif">VITAMIN</text>
    </symbol>
  </defs>

  <!-- Label artwork background -->
  <rect x="172" y="22" width="856" height="956" fill="url(#label-gradient)" role="img" aria-label="Soft green bokeh light background"/>

  <!-- Front title band -->
  <rect x="200" y="210" width="400" height="116" fill="var(--band-dark)"/>
  <rect x="200" y="207" width="400" height="6" fill="url(#rule-gradient)"/>
  <rect x="200" y="323" width="820" height="6" fill="url(#rule-gradient)"/>

  <!-- Dieline and fold guides -->
  <rect class="dieline" x="208" y="60" width="784" height="880"/>
  <line class="fold-line" x1="404" y1="60" x2="404" y2="940"/>
  <line class="fold-line" x1="600" y1="60" x2="600" y2="940"/>
  <line class="fold-line" x1="796" y1="60" x2="796" y2="940"/>

  <!-- Front panel -->
  <g class="front-panel">
    <text class="title-main" x="404" y="271" text-anchor="middle">Antibacterial</text>
    <text class="title-sub" x="404" y="302" text-anchor="middle">HAND WASH</text>

    <use href="#icon-no-germs" x="378" y="375" width="52" height="52"/>
    <text class="icon-caption" x="405" y="444" text-anchor="middle">Anti Bacterial</text>

    <use href="#icon-hands-drop" x="370" y="471" width="70" height="54"/>
    <text class="icon-caption" x="404" y="536" text-anchor="middle">Moisturizing</text>

    <use href="#icon-aloe" x="364" y="564" width="80" height="52"/>
    <text class="icon-caption" x="405" y="631" text-anchor="middle">Anti Bacterial</text>

    <use href="#icon-vitamin-drop" x="384" y="656" width="40" height="50"/>
    <text class="icon-caption" x="404" y="725" text-anchor="middle">Vitamin E</text>

    <rect x="341" y="798" width="127" height="30" rx="15" fill="var(--pill)" stroke="var(--white)" stroke-width="1"/>
    <text class="volume-text" x="404" y="819" text-anchor="middle" font-size="15">8Oz (240ml)</text>
  </g>

  <!-- Back panel -->
  <g class="back-panel">
    <use href="#icon-no-germs" x="710" y="149" width="56" height="56"/>
    <use href="#icon-hands-drop" x="822" y="150" width="72" height="56"/>
    <use href="#icon-aloe" x="696" y="242" width="82" height="56"/>
    <use href="#icon-vitamin-drop" x="836" y="240" width="44" height="54"/>

    <g class="benefit-list">
      <circle cx="746" cy="381" r="2.5" class="icon-fill"/>
      <text class="benefit-item" x="760" y="385">Anti Bacterial</text>
      <circle cx="746" cy="411" r="2.5" class="icon-fill"/>
      <text class="benefit-item" x="760" y="415">Moisturizing</text>
      <circle cx="746" cy="444" r="2.5" class="icon-fill"/>
      <text class="benefit-item" x="760" y="448">Anti Bacterial</text>
      <circle cx="746" cy="474" r="2.5" class="icon-fill"/>
      <text class="benefit-item" x="760" y="478">Vitamin E</text>
      <circle cx="746" cy="504" r="2.5" class="icon-fill"/>
      <text class="benefit-item" x="760" y="508">Other Natural</text>
      <text class="benefit-item" x="760" y="525">Ingredient</text>
    </g>

    <text class="back-title" x="795" y="583" text-anchor="middle">Antibacterial</text>
    <text class="back-sub" x="795" y="601" text-anchor="middle">HAND WASH</text>

    <rect x="745" y="631" width="100" height="23" rx="11.5" fill="var(--pill)" stroke="var(--white)" stroke-width="1"/>
    <text class="volume-text" x="795" y="647" text-anchor="middle" font-size="12">8Oz (240ml)</text>
  </g>

  <!-- Dimensions -->
  <g class="dimensions">
    <line class="dimension-line" x1="212" y1="886" x2="596" y2="886" marker-start="url(#arrow-head)" marker-end="url(#arrow-head)"/>
    <text class="dimension-text" x="404" y="922" text-anchor="middle">3"</text>

    <line class="dimension-line" x1="212" y1="946" x2="988" y2="946" marker-start="url(#arrow-head)" marker-end="url(#arrow-head)"/>
    <text class="dimension-text" x="604" y="982" text-anchor="middle">6"</text>

    <line class="dimension-line" x1="1005" y1="62" x2="1005" y2="938" marker-start="url(#arrow-head)" marker-end="url(#arrow-head)"/>
    <text class="dimension-text" x="0" y="0" text-anchor="middle" font-size="40" transform="translate(1044,462) rotate(-90)">6.75"</text>
  </g>
</svg>
</body>
</html>
```